Red Kettle Pictures BIz Card

This will be a biz card for our independent film company
RED KETTLE PICTURES

we have a logo and i need to figure out how to post it to you!

Here is the info we need on the card:

LOGO

dorinda pratchek (lower case!)
dP@RedKettlePix.example
512-684-2273

Red Kettle Pictures, LLC
www.RedKettlePix.example

stories that matter (tagline)

Target Market(s)

adults in the entertainment industry in USA.
need something creative feeling, a bit funky, not to overt.
something eye catchy that people will be inclined to keep.

ask me any questions you have!

Industry/Entity Type

It Company

Requirements
Must have
• good looking! clean and easy to get the contact info. not too busy.
Nice to have
• love the cards where the design is "continued" on the back side.

perhaps the tag and logo on the back side?!?

open to ideas!
Should not have
• nothing "cartoonish"

```html
<!DOCTYPE html>
<html lang="en">
<head>
<meta charset="utf-8">
<title>Red Kettle Pictures – Business Card</title>
<link rel="stylesheet" href="https://fonts.googleapis.com/css2?family=Arimo:wght@400;700&family=Source+Sans+3:wght@300;400&display=swap">
<style>
  :root {
    --stage: #58585a;
    --red-bright: #ed1c24;
    --red-mid: #b41b21;
    --red-deep: #8a1418;
    --paper: #ffffff;
    --paper-cool: #f6f7f9;
    --ink: #231f20;
    --ink-soft: #4d4d4f;
    --white: #ffffff;
  }
  html, body {
    margin: 0;
    padding: 0;
    width: 1200px;
    height: 900px;
    overflow: hidden;
    background: var(--stage);
  }
  .sheet {
    position: relative;
    width: 1200px;
    height: 900px;
    display: flex;
    flex-direction: column;
    align-items: center;
    justify-content: center;
    gap: 60px;
  }
  .card {
    display: block;
    width: 640px;
    height: 365px;
  }
  .name {
    font-family: "Arimo", Arial, sans-serif;
    font-weight: 700;
    font-size: 24px;
    fill: var(--white);
    letter-spacing: 0.5px;
  }
  .contact {
    font-family: "Arimo", Arial, sans-serif;
    font-weight: 700;
    font-size: 15px;
    fill: var(--white);
  }
  .wordmark {
    font-family: "Arimo", Arial, sans-serif;
    font-weight: 700;
    font-size: 24px;
    fill: var(--ink);
  }
  .wordmark-dot { fill: var(--red-bright); }
  .tagline {
    font-family: "Source Sans 3", "Myriad Pro", sans-serif;
    font-weight: 400;
    font-size: 30px;
    fill: var(--white);
  }
  .company {
    font-family: "Arimo", Arial, sans-serif;
    font-weight: 700;
    font-size: 20px;
    fill: var(--ink-soft);
  }
  .stop-bright { stop-color: var(--red-bright); }
  .stop-mid { stop-color: var(--red-mid); }
  .stop-deep { stop-color: var(--red-deep); }
  .paper { fill: var(--paper); }
  .paper-cool { fill: var(--paper-cool); }
  .side-strip { fill: var(--red-deep); }
</style>
</head>
<body>
<main class="sheet">

  <!-- Front of card -->
  <svg class="card card-front" viewBox="0 0 692 395" xmlns="http://www.w3.org/2000/svg">
    <defs>
      <linearGradient id="front-base" x1="0" y1="0" x2="1" y2="0">
        <stop offset="0" class="stop-bright"/>
        <stop offset="0.34" class="stop-mid"/>
        <stop offset="1" class="stop-deep"/>
      </linearGradient>
      <linearGradient id="front-panel" x1="0" y1="0" x2="1" y2="0">
        <stop offset="0" class="stop-deep"/>
        <stop offset="1" class="stop-bright"/>
      </linearGradient>
    </defs>
    <rect class="card-base" width="692" height="395" fill="url(#front-base)"/>
    <path class="contact-panel" d="M232 395 V180 Q232 90 330 55 L585 55 V395 Z" fill="url(#front-panel)"/>
    <rect class="side-strip" x="585" y="0" width="107" height="395"/>
    <path class="logo-tab paper" d="M328 0 H661 V169 Q661 249 581 249 H408 Q328 249 328 169 Z"/>
    <g class="wordmark-lockup">
      <circle class="wordmark-dot" cx="358" cy="114" r="9"/>
      <text class="wordmark" x="373" y="122">Red Kettle Pictures</text>
    </g>
    <text class="name" x="416" y="305" text-anchor="middle">dorinda pratchek</text>
    <text class="contact" x="416" y="340" text-anchor="middle">dP@RedKettlePix.example</text>
    <text class="contact" x="416" y="363" text-anchor="middle">512-684-2273</text>
  </svg>

  <!-- Back of card -->
  <svg class="card card-back" viewBox="0 0 692 395" xmlns="http://www.w3.org/2000/svg">
    <defs>
      <linearGradient id="back-base" x1="0" y1="0" x2="1" y2="0">
        <stop offset="0" class="stop-bright"/>
        <stop offset="0.45" class="stop-mid"/>
        <stop offset="1" class="stop-deep"/>
      </linearGradient>
    </defs>
    <rect class="card-base" width="692" height="395" fill="url(#back-base)"/>
    <text class="tagline" x="348" y="207" text-anchor="middle">stories that matter</text>
    <path class="company-tab paper-cool" d="M163 395 V349 Q163 279 233 279 H460 Q530 279 530 349 V395 Z"/>
    <text class="company" x="346" y="334" text-anchor="middle">Red Kettle Pictures, LLC</text>
    <text class="company" x="346" y="365" text-anchor="middle">www.RedKettlePix.example</text>
  </svg>

</main>
</body>
</html>
```